GIlbeto Shop Business Card Design

My auto shop is targeted to the European and Asian luxury automotive market. We do mechanics collision and parts.
Some of the makes are KRT, DZ, Vale Strider, Quendel,Morva, solvana, telira, RP, etc. But in the end we get all makes.
I don't want to have the makes logos on the business card.
The Name of the business is after my first Name Gilberto but without the s Gilbeto Shop if there is any other ideas about the name iam open to suggestions. And i don't have a LOGO. Need logo!

Reason: I increased my budget and invited more designers. And committed payment so giving you guys more time.

Target Market(s)

target is the luxury auto market

Industry/Entity Type

Automotive

Contact Information for Business Card

European Automotive Repair Shop, Collision Mechanics Parts
Gilberto Montaño Owner, Pinoverde #9 Loma Seca 2

Requirements
Nice to have
• One design i can of liked was the use of the dash error logos like check engine light airbag light. Nordel press has this but dose not include the air bag light. For the collision part of the business. But am open to any design.
Should not have
• exact logo makes on front of card.

```html
<!DOCTYPE html>
<html lang="en">
<head>
<meta charset="utf-8">
<title>Gilbeto Shop Business Card</title>
<link rel="stylesheet" href="https://fonts.googleapis.com/css2?family=Didact+Gothic&family=Cinzel:wght@400&display=swap">
<style>
  :root {
    --canvas: #ffffff;
    --front-light: #ececec;
    --front-edge: #afadaf;
    --back-dark: #5f5f63;
    --band-light: #d6d6d6;
    --band-edge: #a9a8aa;
    --ink-dark: #545458;
    --mark: #2b2b2d;
    --name-red: #9b1c24;
  }
  * { margin: 0; padding: 0; box-sizing: border-box; }
  html, body {
    width: 1200px;
    height: 378px;
    overflow: hidden;
    background: var(--canvas);
  }
  .canvas {
    position: relative;
    width: 1200px;
    height: 378px;
  }
  .card {
    position: absolute;
    top: 42px;
    width: 505px;
    height: 287px;
    overflow: hidden;
  }
  .card-front {
    left: 66px;
    background: radial-gradient(circle at 50% 48%, var(--front-light) 0%, #d2d1d2 40%, var(--front-edge) 100%);
  }
  .brand {
    position: absolute;
    left: 0;
    right: 0;
    top: 78px;
    display: flex;
    flex-direction: column;
    align-items: center;
  }
  .brand-dot {
    width: 62px;
    height: 62px;
    border-radius: 50%;
    background: var(--mark);
    margin-bottom: 14px;
  }
  .brand-name {
    font-family: "Cinzel", serif;
    font-weight: 400;
    font-size: 18px;
    color: var(--name-red);
    letter-spacing: 0.3px;
  }
  .brand-tagline {
    margin-top: 6px;
    font-family: "Cinzel", serif;
    font-size: 10px;
    color: var(--mark);
  }
  .card-back {
    left: 629px;
    background: var(--back-dark);
  }
  .info-band {
    position: absolute;
    left: 0;
    right: 0;
    top: 100px;
    height: 87px;
    background: radial-gradient(ellipse at 50% 50%, var(--band-light) 0%, #c3c2c3 55%, var(--band-edge) 100%);
    display: flex;
    flex-direction: column;
    align-items: center;
    justify-content: center;
    font-family: "Didact Gothic", sans-serif;
    color: var(--ink-dark);
    text-align: center;
  }
  .info-title {
    font-size: 16.5px;
    letter-spacing: 0.9px;
    text-transform: uppercase;
    margin-bottom: 7px;
  }
  .info-line {
    font-size: 14px;
    letter-spacing: 0.3px;
    line-height: 20px;
  }
</style>
</head>
<body>
<div class="canvas">
  <section class="card card-front">
    <div class="brand">
      <div class="brand-dot"></div>
      <div class="brand-name">GILBERTO MONTAÑO OWNER</div>
      <div class="brand-tagline">European Automotive Repair Shop</div>
    </div>
  </section>

  <section class="card card-back">
    <div class="info-band">
      <h1 class="info-title" style="font-weight:400">European Automotive Repair Shop</h1>
      <p class="info-line">Collision Mechanics Parts Gilberto Montaño Owner</p>
      <p class="info-line">Pinoverde #9 Loma Seca 2</p>
    </div>
  </section>
</div>
</body>
</html>
```